New Signage Design Project

Real estate company looking for signage, PowerPoint and stationery branding. Signs will be placed in front of homes and other properties being sold

Name of company is Tern Haven, LLC

Requirements
Must have
• Name of company - Tern Haven, LLC

```html
<!DOCTYPE html>
<html lang="en">
<head>
<meta charset="utf-8">
<title>Tern Haven, LLC — Business Card</title>
<link rel="stylesheet" href="https://fonts.googleapis.com/css2?family=Arimo:wght@400;700&family=Montserrat:wght@800&family=Source+Sans+3:wght@400&display=swap">
<style>
  :root {
    --card-dark: #223032;
    --accent-teal: #7f9e9f;
    --accent-red: #e4505e;
    --stripe-light: #e6e6e8;
    --paper: #ffffff;
    --label-ink: #111111;
  }
  * { margin: 0; padding: 0; box-sizing: border-box; }
  html, body {
    width: 1200px; height: 425px; overflow: hidden;
    background: var(--paper);
  }
  .sheet { position: relative; width: 1200px; height: 425px; }
  .side-label {
    position: absolute; top: 17px; width: 534px; text-align: center;
    font-family: "Source Sans 3", sans-serif; font-size: 26px; color: var(--label-ink);
  }
  .side-label--front { left: 54px; }
  .side-label--back { left: 614px; }

  .card {
    position: absolute; top: 61px; width: 534px; height: 305px;
    background: var(--card-dark); overflow: hidden;
  }
  .card--front { left: 54px; }
  .card--back { left: 614px; }

  .name-band {
    position: absolute; left: 0; top: 40px; width: 100%; height: 56px;
    background: var(--paper);
    display: flex; align-items: center; justify-content: center;
    padding-right: 20px;
  }
  .name-band__name {
    font-family: "Arimo", sans-serif; font-weight: 700; font-size: 27px;
    color: var(--card-dark); letter-spacing: 0.3px;
  }

  .stripes { position: absolute; inset: 0; width: 100%; height: 100%; }

  .brand { position: absolute; display: flex; flex-direction: column; align-items: center; }
  .brand__dot { border-radius: 50%; background: var(--accent-red); }
  .brand__name {
    font-family: "Montserrat", sans-serif; font-weight: 800;
    color: var(--paper); white-space: nowrap; line-height: 1;
  }
  .card--front .brand { left: 20px; top: 160px; width: 190px; }
  .card--front .brand__dot { width: 44px; height: 44px; margin-bottom: 30px; }
  .card--front .brand__name { font-size: 15px; }
  .card--back .brand { left: 30px; top: 96px; width: 250px; }
  .card--back .brand__dot { width: 66px; height: 66px; margin-bottom: 54px; }
  .card--back .brand__name { font-size: 23px; }

  .contacts {
    position: absolute; left: 227px; top: 148px; list-style: none;
    font-family: "Arimo", sans-serif; font-size: 14px; color: var(--paper);
  }
  .contacts__item { display: flex; align-items: flex-start; gap: 8px; height: 25.5px; line-height: 17px; }
  .contacts__item--address { height: auto; }
  .contacts__icon { width: 14px; height: 14px; margin-top: 2px; flex: none; }
</style>
</head>
<body>
<main class="sheet">
  <p class="side-label side-label--front">Front</p>
  <p class="side-label side-label--back">Back</p>

  <section class="card card--front" aria-label="Card front">
    <div class="name-band"><h1 class="name-band__name">Surname Name</h1></div>

    <svg class="stripes" viewBox="0 0 764 436" preserveAspectRatio="none" aria-hidden="true">
      <defs>
        <linearGradient id="fade-front" x1="742" y1="238" x2="580" y2="436" gradientUnits="userSpaceOnUse">
          <stop offset="0" stop-color="var(--stripe-light)"/>
          <stop offset="1" stop-color="var(--card-dark)"/>
        </linearGradient>
      </defs>
      <polygon points="764,52 764,88 665,204 635,204" fill="var(--accent-teal)"/>
      <polygon points="764,115 764,155 653,290 618,290" fill="var(--accent-red)"/>
      <polygon points="723,238 761,238 600,436 562,436" fill="url(#fade-front)"/>
    </svg>

    <div class="brand">
      <span class="brand__dot"></span>
      <span class="brand__name">TERN HAVEN, LLC</span>
    </div>

    <ul class="contacts">
      <li class="contacts__item">
        <svg class="contacts__icon" viewBox="0 0 16 16" fill="none" stroke="currentColor" stroke-width="1.2" aria-hidden="true"><path d="M3 1.5l2.5 0 1.2 3-1.6 1.2c.9 2 2.2 3.3 4.2 4.2l1.2-1.6 3 1.2v2.5c0 .8-.7 1.5-1.5 1.5C6.5 13.5 2.5 9.5 1.5 3c0-.8.7-1.5 1.5-1.5z"/></svg>
        <span>+00 123 456 789</span>
      </li>
      <li class="contacts__item">
        <svg class="contacts__icon" viewBox="0 0 16 16" fill="none" stroke="currentColor" stroke-width="1.2" aria-hidden="true"><rect x="1.5" y="3.5" width="13" height="9"/><path d="M1.5 3.5l6.5 5 6.5-5"/></svg>
        <span>Company@mail.com</span>
      </li>
      <li class="contacts__item">
        <svg class="contacts__icon" viewBox="0 0 16 16" fill="none" stroke="currentColor" stroke-width="1.2" aria-hidden="true"><path d="M8 15s5-5.2 5-8.8A5 5 0 0 0 3 6.2C3 9.8 8 15 8 15z"/><circle cx="8" cy="6.2" r="1.8"/></svg>
        <span>www.website.com</span>
      </li>
      <li class="contacts__item contacts__item--address">
        <svg class="contacts__icon" viewBox="0 0 16 16" fill="none" stroke="currentColor" stroke-width="1.1" aria-hidden="true"><circle cx="8" cy="8" r="6.5"/><ellipse cx="8" cy="8" rx="2.8" ry="6.5"/><path d="M1.5 8h13M2.5 4.8h11M2.5 11.2h11"/></svg>
        <span>148 Willow Ct, Brandon,<br>MS, 39042</span>
      </li>
    </ul>
  </section>

  <section class="card card--back" aria-label="Card back">
    <svg class="stripes" viewBox="0 0 764 436" preserveAspectRatio="none" aria-hidden="true">
      <defs>
        <linearGradient id="fade-back" x1="742" y1="238" x2="580" y2="436" gradientUnits="userSpaceOnUse">
          <stop offset="0" stop-color="var(--stripe-light)"/>
          <stop offset="1" stop-color="var(--card-dark)"/>
        </linearGradient>
      </defs>
      <polygon points="764,52 764,92 668,204 636,204" fill="var(--accent-teal)"/>
      <polygon points="764,112 764,155 650,292 618,292" fill="var(--accent-red)"/>
      <polygon points="723,238 762,238 600,436 562,436" fill="url(#fade-back)"/>
    </svg>

    <div class="brand">
      <span class="brand__dot"></span>
      <span class="brand__name">TERN HAVEN, LLC</span>
    </div>
  </section>
</main>
</body>
</html>
```